High end Electrical/home automation Business Card

Need a card for a high end electrical and home automation company utilising the existing logo.
Phone
Email
Website

Like black look with raised detail. Don’t necessarily need to keep colour of logo it could be made grayscale or white etc

Target Market(s)

High end clients

Contact Information for Business Card

Ridgeline Electrical

Requirements
Must have
• Logo, phone, email, website, address

High end look
Nice to have
• Black background card
Raised font
Should not have
• Lots of colour

```html
<!DOCTYPE html>
<html lang="en">
<head>
<meta charset="utf-8">
<title>Ridgeline Electrical – Business Card</title>
<link rel="stylesheet" href="https://fonts.googleapis.com/css2?family=Montserrat:wght@400;500;600;700&display=swap">
<style>
  :root {
    --backdrop: #4a4e51;
    --card: #15171b;
    --card-deep: #0f1114;
    --blue: #2f8fd8;
    --blue-soft: rgba(47, 143, 216, 0.55);
    --white: #f4f6f8;
    --grey: #c9cdd2;
  }
  * { box-sizing: border-box; margin: 0; padding: 0; }
  html, body {
    width: 1200px; height: 1050px; overflow: hidden;
    background: var(--backdrop);
    font-family: "Montserrat", Arial, sans-serif;
  }
  .sheet {
    width: 1200px; height: 1050px;
    display: flex; flex-direction: column; align-items: center; justify-content: center;
    gap: 60px;
  }
  .card {
    position: relative;
    width: 720px; height: 420px;
    background: var(--card);
    border-radius: 4px;
    overflow: hidden;
    box-shadow: 0 14px 30px rgba(0,0,0,0.35);
  }
  .card-texture {
    position: absolute; inset: 0;
    background: radial-gradient(ellipse at 40% 35%, var(--card) 0%, var(--card-deep) 100%);
  }

  /* Front */
  .front-mark {
    position: absolute; left: 40px; top: 150px;
    display: flex; align-items: center; gap: 10px;
  }
  .mark-dot {
    width: 14px; height: 14px; border-radius: 50%;
    background: var(--blue);
  }
  .mark-name {
    color: var(--white); font-weight: 600; font-size: 20px;
  }
  .front-heading {
    position: absolute; left: 300px; top: 60px;
    color: var(--blue); font-weight: 600; font-size: 20px; letter-spacing: 3.5px;
  }
  .rule {
    position: absolute; height: 1px;
  }
  .rule-top {
    top: 198px; left: 0; width: 280px;
    background: linear-gradient(90deg, transparent, var(--blue-soft) 25%, var(--blue-soft));
  }
  .rule-bottom {
    top: 385px; left: 0; right: 0;
    background: linear-gradient(90deg, transparent, var(--blue-soft) 20%, var(--blue-soft) 80%, transparent);
  }
  .contact {
    position: absolute; left: 300px; top: 112px; width: 380px;
  }
  .person {
    display: flex; align-items: center; gap: 10px;
    color: var(--blue); font-weight: 600; font-size: 13px; letter-spacing: 1.5px;
    margin-bottom: 14px;
  }
  .person::after {
    content: ""; flex: 1; height: 1px; background: var(--blue);
  }
  .contact-row {
    display: flex; align-items: center; gap: 14px;
    font-size: 15px; color: var(--white);
    margin-bottom: 11px;
  }
  .contact-row svg { width: 18px; height: 18px; flex: none; }
  .accent { color: var(--blue); }
  .address {
    position: absolute; left: 110px; top: 330px;
    display: flex; align-items: center; gap: 14px;
    font-size: 16px; color: var(--white);
  }
  .address svg { width: 18px; height: 22px; }

  /* Back */
  .back-mark {
    position: absolute; inset: 0;
    display: flex; align-items: center; justify-content: center; gap: 14px;
  }
  .back-mark .mark-dot { width: 22px; height: 22px; }
  .back-mark .mark-name { font-size: 40px; }
</style>
</head>
<body>
<main class="sheet">
  <section class="card card-front">
    <div class="card-texture" role="img" aria-label="Fine dark woven texture across the card"></div>
    <div class="front-mark">
      <span class="mark-dot"></span>
      <span class="mark-name">Ridgeline Electrical</span>
    </div>
    <div class="rule rule-top"></div>
    <h1 class="front-heading">RIDGELINE ELECTRICAL</h1>
    <div class="contact">
      <p class="person">PERSON NAME</p>
      <p class="contact-row">
        <svg viewBox="0 0 18 18" fill="none" stroke="var(--blue)" stroke-width="1.4"><rect x="5" y="1.5" width="8" height="15" rx="1.5"/><line x1="7.5" y1="13.5" x2="10.5" y2="13.5"/></svg>
        <span>021 480 372 - <span class="accent">0800 61 72 40</span></span>
      </p>
      <p class="contact-row">
        <svg viewBox="0 0 18 18" fill="none" stroke="var(--white)" stroke-width="1.4"><rect x="1.5" y="4" width="15" height="10"/><polyline points="1.5,4 9,10 16.5,4"/></svg>
        <span><span class="accent">info@</span>ridgeline-electrical.co.nz</span>
      </p>
      <p class="contact-row">
        <svg viewBox="0 0 18 18" fill="none" stroke="var(--blue)" stroke-width="1.4"><circle cx="9" cy="9" r="7.5"/><ellipse cx="9" cy="9" rx="3.2" ry="7.5"/><line x1="1.5" y1="9" x2="16.5" y2="9"/></svg>
        <span>www.ridgeline-electrical.<span class="accent">co.nz</span></span>
      </p>
    </div>
    <p class="address">
      <svg viewBox="0 0 18 22" fill="none" stroke="var(--white)" stroke-width="1.4"><path d="M9 1.5a5 5 0 0 1 5 5c0 3.5-5 8.5-5 8.5s-5-5-5-8.5a5 5 0 0 1 5-5z"/><circle cx="9" cy="6.5" r="1.6"/><ellipse cx="9" cy="18.5" rx="7" ry="2.2"/></svg>
      <span><span class="accent">18 Harbour View Road Devonport</span>, Auckland</span>
    </p>
    <div class="rule rule-bottom"></div>
  </section>

  <section class="card card-back">
    <div class="card-texture" role="img" aria-label="Fine dark woven texture across the card"></div>
    <div class="back-mark">
      <span class="mark-dot"></span>
      <span class="mark-name">Ridgeline Electrical</span>
    </div>
  </section>
</main>
</body>
</html>
```